Dog treat bakery needs updated bag labels

We're a small-batch dog treat bakery and would like to update our front bag labels to 1) differentiate our line of products and 2) to stand out on shelves. We believe all dogs deserve to eat clean, healthy foods. That's why we bake low-calorie, clean treats made with simple, premium ingredients like teff, amaranth, and sorghum flours and 100% blueberry, carrot, and purple sweet potato. All our treats are made gluten free without preservatives, artificial flavors, soy, corn, wheat, or eggs. Clean treats, happy dogs!

see uploaded files

```html
<!DOCTYPE html>
<html lang="en">
<head>
<meta charset="utf-8">
<title>Patchy Pup – Maple's Morsels Label</title>
<link href="https://fonts.googleapis.com/css2?family=Bebas+Neue&family=Cormorant+Garamond:wght@600;700&display=swap" rel="stylesheet">
<style>
  :root {
    --teal: #1b9ba4;
    --charcoal: #333333;
    --white: #ffffff;
    --light-grey: #e6e6e6;
    --page: #ffffff;
  }
  * { margin: 0; padding: 0; box-sizing: border-box; }
  html, body {
    width: 891px;
    height: 1200px;
    overflow: hidden;
    background: var(--page);
  }
  .canvas {
    position: relative;
    width: 891px;
    height: 1200px;
  }
  .label {
    position: absolute;
    left: 46px;
    top: 369px;
    width: 798px;
    height: 462px;
    background: var(--teal);
    overflow: hidden;
  }
  .center-band {
    position: absolute;
    left: 0;
    top: 0;
    width: 798px;
    height: 462px;
  }
  .heart-art {
    position: absolute;
    left: 22px;
    top: 36px;
    width: 202px;
    height: 398px;
    border-radius: 40px;
    background: linear-gradient(180deg, rgba(255,255,255,0.16), rgba(255,255,255,0.08));
  }
  .tagline {
    position: absolute;
    left: 214px;
    width: 352px;
    top: 14px;
    text-align: center;
    font-family: "Cormorant Garamond", serif;
    font-weight: 700;
    font-size: 24px;
    letter-spacing: 1.5px;
    color: var(--teal);
  }
  .product-type {
    position: absolute;
    left: 214px;
    width: 352px;
    top: 46px;
    text-align: center;
    font-family: "Bebas Neue", sans-serif;
    font-weight: 400;
    font-size: 48px;
    line-height: 1;
    color: var(--white);
  }
  .brand-seal {
    position: absolute;
    left: 261px;
    top: 116px;
    width: 256px;
    height: 256px;
    border-radius: 50%;
    background: var(--white);
    display: flex;
    align-items: center;
    justify-content: center;
  }
  .brand-name {
    font-family: "Bebas Neue", sans-serif;
    font-size: 44px;
    line-height: 1;
    letter-spacing: 2px;
    color: var(--teal);
  }
  .product-name {
    position: absolute;
    left: 214px;
    width: 352px;
    top: 381px;
    text-align: center;
    font-family: "Cormorant Garamond", serif;
    font-weight: 700;
    font-size: 30px;
    letter-spacing: 1.5px;
    color: var(--teal);
  }
  .net-weight {
    position: absolute;
    left: 214px;
    width: 352px;
    top: 423px;
    text-align: center;
    font-family: "Cormorant Garamond", serif;
    font-weight: 700;
    font-size: 14px;
    letter-spacing: 0.8px;
    color: var(--white);
  }
  .claims {
    position: absolute;
    left: 600px;
    top: 46px;
    font-family: "Bebas Neue", sans-serif;
    font-size: 25px;
    line-height: 32.5px;
    color: var(--light-grey);
    list-style: none;
  }
  .claims .lead { color: var(--charcoal); }
  .claims .gap { height: 38px; }
  .calorie-pill {
    position: absolute;
    left: 565px;
    top: 388px;
    width: 188px;
    height: 47px;
    border-radius: 24px;
    background: var(--charcoal);
    color: var(--white);
    font-family: "Bebas Neue", sans-serif;
    font-size: 24px;
    line-height: 47px;
    text-align: center;
    letter-spacing: 0.3px;
  }
</style>
</head>
<body>
<main class="canvas">
  <section class="label">
    <div class="heart-art" role="img" aria-label="Cluster of outlined white hearts decoration"></div>

    <svg class="center-band" viewBox="0 0 798 462" aria-hidden="true">
      <path d="M278 0 H502 C522 90 566 150 566 230 C566 310 522 370 502 462 H278 C258 370 216 310 216 230 C216 150 258 90 278 0 Z" fill="#333333"/>
      <g fill="#ffffff">
        <circle cx="267" cy="131" r="2.5"/>
        <circle cx="295" cy="128" r="3.5"/>
        <circle cx="281" cy="152" r="2.5"/>
        <circle cx="263" cy="167" r="3.5"/>
        <circle cx="512" cy="137" r="3.5"/>
        <circle cx="495" cy="157" r="2"/>
        <circle cx="521" cy="183" r="3.5"/>
        <circle cx="279" cy="335" r="4"/>
        <circle cx="286" cy="364" r="3"/>
        <circle cx="316" cy="381" r="2"/>
        <circle cx="513" cy="343" r="4.5"/>
        <circle cx="476" cy="373" r="3"/>
      </g>
    </svg>

    <p class="tagline">gluten free</p>
    <h1 class="product-type">Dog Treats</h1>

    <div class="brand-seal">
      <p class="brand-name">Patchy Pup</p>
    </div>

    <h2 class="product-name">Maple’s Morsels</h2>
    <p class="net-weight">Net Wt 4 OZ (113g)</p>

    <ul class="claims">
      <li class="lead">No</li>
      <li>Soy, Corn,</li>
      <li>Wheat, Eggs</li>
      <li>or Dairy</li>
      <li class="gap"></li>
      <li class="lead">Made With</li>
      <li>Ancient Grains</li>
      <li>and Grass Fed</li>
      <li>Beef Liver</li>
    </ul>

    <div class="calorie-pill">10 Calories Each</div>
  </section>
</main>
</body>
</html>
```